Bright Harbor
Creative Brief
Simple
RT Vell, MD
President
27415 Maple Orchard Way 300B
Alder Ridge, OH 45099
rvell@brightharb.example
www.brightharb.example
1. Please incorporate a watermark of our logo on the stationary
no specs
halvora medical center
Concepts
Steady Path Body Wellness (logo uploaded)
Tremaxo
Company name: Vigor Summit
try and keep the color scheme of the logo: purple and grey in the design.
oh, and no black please.
thank you for the submissions, I think we will have a winner soon. our design tastes are simple:
1. keep the design simple, functional and professional
2. keep the font size large enough to so they can be read when printed.
3. keep in mind when changes are made to contact info the style should be the same
4. some space on front to write is nice
5. we will want a word document file of the final draft
6. stationary should be simple with logo at top (try left side corner), watermark in the center of page, and address at top and/or bottom (show both). no need for extra purple borders.
7. folder purple back and simple front.
ALL:
pls note my email should read rvell@brightharb.example
(the system would not let me type it this way)

```html
<!DOCTYPE html>
<html lang="en">
<head>
<meta charset="utf-8">
<title>Bright Harbor Stationery</title>
<link href="https://fonts.googleapis.com/css2?family=Source+Sans+3:wght@400;600&display=swap" rel="stylesheet">
<style>
:root{
  --stage:#333335;
  --purple:#6b2a8e;
  --purple-soft:#eee8f2;
  --paper:#f7f7f8;
  --paper-shade:#e6e6e8;
  --ink:#4a4a4f;
  --ink-light:#7a7a80;
  --label:#e8e8e8;
}
*{margin:0;padding:0;box-sizing:border-box}
html,body{width:1200px;height:372px;overflow:hidden;background:var(--stage)}
body{font-family:"Source Sans 3",Arial,sans-serif;color:var(--ink);position:relative}
.piece{position:absolute;background:var(--paper);overflow:hidden}
.label{position:absolute;color:var(--label);font-size:5.6px;text-align:center;width:140px}
.brand{color:var(--purple);font-weight:600;line-height:1;white-space:nowrap;display:flex;align-items:center;gap:2px}
.brand .dot{display:inline-block;border-radius:50%;background:var(--purple)}
.faint-mark{position:absolute;border-radius:50%;background:var(--purple-soft)}
.tiny{font-size:3px;line-height:1.45;color:var(--ink-light);white-space:nowrap}
.icon{display:inline-block;width:2.4px;height:2.4px;background:var(--ink-light);margin-right:1.5px;vertical-align:middle;border-radius:.5px}
/* letterheads */
.letterhead{width:217px;height:280px}
.letterhead .brand{font-size:9px}
.letter-body{position:absolute;left:15px;top:60px;width:180px;font-size:3.4px;line-height:1.5;color:var(--ink)}
.letter-body p{margin-bottom:5px}
.letter-body .strong{font-weight:600}
.signature{width:45px;height:10px;background:#d9d9dc;border-radius:2px;margin:2px 0}
.sign-name{color:var(--purple);font-weight:600;font-size:4.2px}
.web-foot{position:absolute;bottom:8px;width:100%;text-align:center;font-size:3px;letter-spacing:1px;color:var(--ink-light)}
/* envelope */
.envelope{width:234px;height:135px;border-radius:3px 3px 0 0}
.env-flap{position:absolute;left:0;top:0;width:100%;height:34px;background:linear-gradient(#f2f2f3,#ececee);border-bottom:1px solid var(--paper-shade)}
/* cards */
.card{width:130px;height:73px}
.card .brand{font-size:8.5px;position:absolute;right:6px;top:12px}
.card-name{position:absolute;left:7px;top:34px;color:var(--purple);font-weight:600;font-size:5px}
.card-role{position:absolute;left:7px;top:40px;font-size:3.6px;color:var(--ink-light)}
.card-rule{position:absolute;left:7px;right:6px;top:45px;height:.5px;background:#bbb}
.card-contact{position:absolute;left:7px;top:47px}
.card-address{position:absolute;right:6px;top:58px;text-align:right}
.card-back{background:var(--purple)}
.card-back .brand{color:#fff;font-size:11px;position:absolute;left:0;right:0;top:26px;justify-content:center}
.card-back .brand .dot{background:#fff}
.card-back .web{position:absolute;bottom:10px;width:100%;text-align:center;color:#e6dcef;font-size:3px;letter-spacing:1.6px}
/* folder */
.folder-back{background:var(--purple);width:171px;height:287px}
.folder-back .tiny{color:#eadff2;position:absolute;left:6px;bottom:16px;font-size:3.4px}
.folder-back .icon{background:#eadff2}
.folder-front{width:170px;height:284px;background:linear-gradient(135deg,#fafafa,#e4e4e6)}
.folder-front .brand{font-size:15px;position:absolute;left:0;right:0;top:136px;justify-content:center}
.folder-inner{width:287px;height:267px;background:#f3f3f4}
.inner-fold{position:absolute;left:143px;top:0;width:1px;height:100%;background:#d6d6d9}
.pocket{position:absolute;bottom:0;height:88px;background:var(--purple)}
.pocket-left{left:0;width:135px;border-radius:0 8px 0 0}
.pocket-right{right:0;width:135px;border-radius:8px 0 0 0}
.slot-card{position:absolute;right:38px;bottom:54px;width:62px;height:34px;background:var(--paper)}
.slot-card .brand{font-size:5px;position:absolute;right:3px;top:6px}
</style>
</head>
<body>

<!-- Letterhead option 02 (behind) -->
<section class="piece letterhead" style="left:143px;top:45px;height:279px">
  <div class="faint-mark" style="left:70px;top:110px;width:80px;height:80px"></div>
  <div class="brand" style="position:absolute;left:95px;top:20px;font-size:9px"><span class="dot" style="width:5px;height:5px"></span>Bright Harbor</div>
  <div class="tiny" style="position:absolute;left:98px;bottom:12px">27415 Maple Orchard Way 300B, Alder Ridge, OH 45099<br>E: rvell@brightharb.example W: www.brightharb.example</div>
</section>

<!-- Letterhead option 01 -->
<section class="piece letterhead" style="left:26px;top:64px">
  <div class="faint-mark" style="left:70px;top:110px;width:80px;height:80px"></div>
  <div class="brand" style="position:absolute;left:15px;top:22px"><span class="dot" style="width:5px;height:5px"></span>Bright Harbor</div>
  <div class="tiny" style="position:absolute;left:156px;top:14px">27415 Maple Orchard Way 300B<br>Alder Ridge, OH 45099<br><span class="icon"></span>555 014 2276<br><span class="icon"></span>555 019 8314<br><span class="icon"></span>rvell@brightharb.example</div>
  <div class="letter-body">
    <p>Date</p>
    <p class="strong">Recipient Name</p>
    <p>Company Name<br>Street Address<br>City, State, Zip</p>
    <p style="margin-top:10px">Thank you for choosing our clinic for your care. This letter confirms the details of your next visit and the steps we will take together.</p>
    <p>Please arrive a few minutes early and bring any recent records. Our staff will gladly answer questions before your appointment begins.</p>
    <p>We look forward to working with you and supporting your goals throughout the program.</p>
    <p>Kind regards from the whole team.</p>
    <p style="margin-top:8px;margin-bottom:1px">Sincerely,</p>
    <div class="signature" role="img" aria-label="Handwritten signature"></div>
    <div class="sign-name">RT Vell, MD</div>
    <div style="color:var(--ink-light)">President</div>
  </div>
  <div class="web-foot">www.brightharb.example</div>
</section>
<div class="label" style="left:57px;top:350px">Letterhead_Option_01</div>
<div class="label" style="left:228px;top:333px">Letterhead_Option_02</div>

<!-- Envelope -->
<section class="piece envelope" style="left:185px;top:156px">
  <div class="env-flap"></div>
  <div class="tiny" style="position:absolute;left:0;right:0;top:6px;text-align:center;transform:rotate(180deg)">www.brightharb.example</div>
  <span style="position:absolute;left:114px;top:16px;width:6px;height:6px;border-radius:50%;background:var(--purple)"></span>
  <div class="faint-mark" style="left:168px;top:52px;width:58px;height:58px"></div>
  <div class="brand" style="position:absolute;left:11px;top:46px;font-size:8px"><span class="dot" style="width:4px;height:4px"></span>Bright Harbor</div>
  <div class="tiny" style="position:absolute;left:23px;top:56px">27415 Maple Orchard Way 300B<br>Alder Ridge, OH 45099</div>
</section>

<!-- Email signature -->
<section class="piece card" style="left:391px;top:18px;width:144px;height:69px">
  <div class="brand" style="position:absolute;right:8px;top:12px;font-size:8.5px"><span class="dot" style="width:5px;height:5px"></span>Bright Harbor</div>
  <div class="card-name" style="top:29px">RT Vell, MD</div>
  <div class="card-role" style="top:35px">President</div>
  <div class="card-rule" style="top:41px;right:9px"></div>
  <div class="card-contact tiny" style="top:43px"><span class="icon"></span>555 014 2276<br><span class="icon"></span>555 019 8314<br><span class="icon"></span>rvell@brightharb.example<br><span class="icon"></span>www.brightharb.example</div>
  <div class="card-address tiny" style="right:9px;top:54px">27415 Maple Orchard Way 300B<br>Alder Ridge, OH 45099</div>
</section>
<div class="label" style="left:393px;top:90px">Email Signature</div>

<!-- Front card -->
<section class="piece card" style="left:432px;top:103px">
  <div class="brand"><span class="dot" style="width:5px;height:5px"></span>Bright Harbor</div>
  <div class="card-name">RT Vell, MD</div>
  <div class="card-role">President</div>
  <div class="card-rule"></div>
  <div class="card-contact tiny"><span class="icon"></span>555 014 2276<br><span class="icon"></span>555 019 8314<br><span class="icon"></span>rvell@brightharb.example<br><span class="icon"></span>www.brightharb.example</div>
  <div class="card-address tiny">27415 Maple Orchard Way 300B<br>Alder Ridge, OH 45099</div>
</section>
<div class="label" style="left:427px;top:179px">Front card_01</div>

<!-- Back cards -->
<section class="piece card card-back" style="left:432px;top:191px">
  <div class="brand"><span class="dot" style="width:6px;height:6px"></span>Bright Harbor</div>
  <div class="web">www.brightharb.example</div>
</section>
<div class="label" style="left:427px;top:268px">Back card_01</div>

<section class="piece card card-back" style="left:432px;top:280px">
  <div class="brand"><span class="dot" style="width:6px;height:6px"></span>Bright Harbor</div>
  <div class="web">www.brightharb.example</div>
</section>
<div class="label" style="left:427px;top:355px">Back card_02</div>

<!-- Folder back -->
<section class="piece folder-back" style="left:574px;top:60px">
  <div class="tiny">27415 Maple Orchard Way 300B<br>Alder Ridge, OH 45099<br><span class="icon"></span>555 014 2276<br><span class="icon"></span>555 019 8314<br><span class="icon"></span>rvell@brightharb.example</div>
</section>
<div class="label" style="left:580px;top:350px">Folder_Back</div>

<!-- Folder front -->
<section class="piece folder-front" style="left:634px;top:33px">
  <div class="brand"><span class="dot" style="width:8px;height:8px"></span>Bright Harbor</div>
</section>
<div class="label" style="left:701px;top:326px">Folder_Front</div>

<!-- Folder inner -->
<section class="piece folder-inner" style="left:892px;top:48px">
  <div class="faint-mark" style="left:30px;top:50px;width:80px;height:80px"></div>
  <div class="faint-mark" style="left:180px;top:50px;width:80px;height:80px"></div>
  <div class="inner-fold"></div>
  <div class="pocket pocket-left"></div>
  <div class="pocket pocket-right"></div>
  <div class="slot-card">
    <div class="brand"><span class="dot" style="width:3px;height:3px"></span>Bright Harbor</div>
    <div style="position:absolute;left:3px;top:16px;font-size:2.6px;color:var(--purple);font-weight:600">RT Vell, MD</div>
    <div style="position:absolute;left:3px;top:20px;font-size:2px;color:var(--ink-light);line-height:1.4">555 014 2276<br>555 019 8314<br>rvell@brightharb.example</div>
  </div>
</section>
<div class="label" style="left:953px;top:319px">Folder_Inner</div>

</body>
</html>
```